Brightvale Inc. Business Card Design

Brightvale Inc. is in search of a great clean design for our business cards!

Looking to incorporate our full logo and watermark on side one (however, I am open to having the text and watermark separated within the design.)

On side two, I am looking to have contact information (Name, Position, Phone #, Email, Website (www.thebrightvale.ca). Can have the logo and/or watermark as part of the design if applicable.

Please add tagline "Where Shine Counts" on either side 1 or 2. This tagline can be in a sans serif, serif or cursive font as long as it compliments overall design. Capitalization can be title or sentence case depending on how it fits within the design.

Get creative!! Looking for a clean, crisp, premium design! Looking for a glossy card finish with spot UV features when printed. Cards will also be printed with rounded corners. Standard dimensions (3.5 x 2).

Target Market(s)

B2B - primary clients are business owners or property management corporations. (residential jobs are few and far between)

Industry/Entity Type

Business

Contact Information for Business Card

- clean, crisp design
- double sided
- spot UV accents and glossy finish upon printing
- standard business card size (3.5 x 2) with rounded corners
- please see project description for requirements per side

Font styles to use
Sans Serif

Requirements
Must have
• - adequate bleeds with print ready files
• - cohesive design elements between side 1 & 2
• - spot UV elements (can be on both sides or just one, use your discretion)
• - colour pallet should match the logo file provided
• - incorporate tagline "where shine counts" (this tagline can be in a serif or sans serif font as long as it is complimentary to the overall design.
Nice to have
• - Premium elements with a clean design
Should not have
• - Please omit cartoon or whimsical like designs, think premium.
• - Colours should not stray from the pallet of the provided logo.

```html
<!DOCTYPE html>
<html lang="en">
<head>
<meta charset="utf-8">
<title>Brightvale Inc. Business Card</title>
<link rel="stylesheet" href="https://fonts.googleapis.com/css2?family=Open+Sans:wght@400;600;700&display=swap">
<style>
  :root {
    --stage: #dcebf5;
    --card-front: #f4f6f7;
    --card-back: #1a6a99;
    --navy: #141a5a;
    --teal: #48e8b9;
    --grey: #9aa3ab;
    --splash-light: #e9f3fa;
    --splash-mid: #8cc4ea;
    --splash-deep: #3f8fd0;
  }
  * { box-sizing: border-box; margin: 0; padding: 0; }
  html, body {
    width: 1200px;
    height: 1200px;
    overflow: hidden;
    background: var(--stage);
    font-family: "Open Sans", Arial, sans-serif;
  }
  .card { position: absolute; overflow: hidden; }
  .card--front {
    left: 258px; top: 130px; width: 717px; height: 430px;
    background: linear-gradient(180deg, #eef1f3 0%, var(--card-front) 40%, #fafbfc 100%);
  }
  .card--back {
    left: 255px; top: 602px; width: 726px; height: 436px;
    background: var(--card-back);
  }
  .front-brand {
    position: absolute; left: 0; right: 0; top: 92px;
    display: flex; align-items: center; justify-content: center; gap: 18px;
  }
  .brand-mark { display: block; background: var(--teal); }
  .front-brand .brand-mark { width: 58px; height: 58px; }
  .front-brand .brand-name {
    font-size: 62px; font-weight: 700; color: var(--navy);
    letter-spacing: -1px; line-height: 1;
  }
  .tagline {
    position: absolute; left: 0; right: 0; top: 176px;
    text-align: center; font-size: 20px; font-weight: 600;
    letter-spacing: 4px; text-transform: uppercase; color: var(--grey);
  }
  .splash-area {
    position: absolute; left: 0; right: 0; bottom: 0; height: 208px;
    background:
      radial-gradient(ellipse 30% 70% at 62% 100%, var(--splash-deep) 0%, rgba(63,143,208,0) 100%),
      radial-gradient(ellipse 22% 60% at 15% 100%, var(--splash-mid) 0%, rgba(140,196,234,0) 100%),
      linear-gradient(180deg, rgba(233,243,250,0) 0%, var(--splash-light) 100%);
  }
  .back-brand {
    position: absolute; left: 40px; width: 320px; top: 92px;
    display: flex; flex-direction: column; align-items: center; gap: 20px;
  }
  .back-brand .brand-mark { width: 80px; height: 80px; }
  .back-brand .brand-name {
    font-size: 40px; font-weight: 700; color: var(--teal);
    letter-spacing: -0.5px; line-height: 1; white-space: nowrap;
  }
  .person { text-align: center; line-height: 1.3; }
  .person-name { font-size: 20px; font-weight: 700; color: #ffffff; }
  .person-role { font-size: 15px; font-weight: 400; color: var(--teal); }
  .divider {
    position: absolute; left: 389px; top: 94px;
    width: 2px; height: 240px; background: var(--navy);
  }
  .contact-list { position: absolute; left: 410px; top: 112px; list-style: none; }
  .contact-item {
    display: flex; align-items: center; gap: 14px;
    height: 30px; margin-bottom: 32px;
    color: var(--navy); font-size: 17px; white-space: nowrap;
  }
  .contact-item svg { width: 30px; height: 30px; flex: none; }
</style>
</head>
<body>

<section class="card card--front" aria-label="Business card front">
  <div class="front-brand">
    <span class="brand-mark" aria-hidden="true"></span>
    <span class="brand-name">Brightvale Inc.</span>
  </div>
  <p class="tagline">Where Shine Counts</p>
  <div class="splash-area" role="img" aria-label="Photograph of splashing clear water across the lower card"></div>
</section>

<section class="card card--back" aria-label="Business card back">
  <div class="back-brand">
    <span class="brand-mark" aria-hidden="true"></span>
    <span class="brand-name">Brightvale Inc.</span>
    <div class="person">
      <p class="person-name">Jordan Ellis</p>
      <p class="person-role">Operations Manager</p>
    </div>
  </div>
  <div class="divider"></div>
  <ul class="contact-list">
    <li class="contact-item">
      <svg viewBox="0 0 24 24" aria-hidden="true"><path fill="#141a5a" d="M6.6 2.5l3 3.2-1.9 2.4c1.3 2.8 3.4 5 6.2 6.3l2.4-1.9 3.2 3-2 3.2C11 18 5.9 12.9 3.3 6.6z"/></svg>
      <span class="contact-text">(604) 555-0147</span>
    </li>
    <li class="contact-item">
      <svg viewBox="0 0 24 24" aria-hidden="true"><rect x="3" y="6" width="18" height="13" fill="#141a5a"/><path d="M3.5 6.5l8.5 7 8.5-7" fill="none" stroke="#1a6a99" stroke-width="1.6"/></svg>
      <span class="contact-text">hello@thebrightvale.ca</span>
    </li>
    <li class="contact-item">
      <svg viewBox="0 0 24 24" aria-hidden="true"><path fill="#141a5a" d="M12 2a6.5 6.5 0 0 0-6.5 6.5C5.5 13.5 12 20 12 20s6.5-6.5 6.5-11.5A6.5 6.5 0 0 0 12 2zm0 9.2a2.7 2.7 0 1 1 0-5.4 2.7 2.7 0 0 1 0 5.4z"/><ellipse cx="12" cy="21.3" rx="4" ry="1" fill="#141a5a"/></svg>
      <span class="contact-text">120 Harbour Street, Vancouver</span>
    </li>
    <li class="contact-item">
      <svg viewBox="0 0 24 24" aria-hidden="true"><circle cx="12" cy="12" r="9" fill="none" stroke="#141a5a" stroke-width="1.8"/><path d="M3 12h18M12 3c-3 3-3 15 0 18M12 3c3 3 3 15 0 18" fill="none" stroke="#141a5a" stroke-width="1.4"/></svg>
      <span class="contact-text">www.thebrightvale.ca</span>
    </li>
  </ul>
</section>

</body>
</html>
```